Bref créative
Business card and stationery for painting company
Brightcoat finishes
Professional
Marek Dolvan
Owner
318 S Harlow Ave suite 204
Villa Park, IL 60139
marek.dolvan@brightcoatfinishes.com
www.brightcoatfinishes.com
this is file of my logo
vector logo file

```html
<!DOCTYPE html>
<html lang="en">
<head>
<meta charset="utf-8">
<title>Brightcoat finishes — Stationery</title>
<link href="https://fonts.googleapis.com/css2?family=Montserrat:wght@700&family=Open+Sans:wght@400;600&display=swap" rel="stylesheet">
<style>
  :root {
    --backdrop: #ece8e1;
    --paper: #ffffff;
    --brand-red: #d7262b;
    --brand-red-dark: #a9161b;
    --brand-blue: #2b5fb5;
    --ink: #2c2c2c;
    --muted: #7a7a7a;
    --hairline: #d9d9d9;
    --faint: rgba(215, 38, 43, 0.08);
  }
  * { box-sizing: border-box; margin: 0; padding: 0; }
  html, body { width: 1200px; height: 598px; overflow: hidden; }
  body {
    position: relative;
    background: var(--backdrop);
    font-family: "Open Sans", Arial, sans-serif;
    color: var(--ink);
  }
  .brand-name {
    font-family: "Montserrat", Arial, sans-serif;
    font-weight: 700;
    color: var(--brand-red);
    text-transform: uppercase;
    letter-spacing: 0.04em;
    white-space: nowrap;
    display: flex;
    align-items: center;
    gap: 6px;
  }
  .brand-dot { border-radius: 50%; background: var(--brand-red); flex: none; }

  /* Business card */
  .business-card {
    position: absolute; left: 19px; top: 367px; width: 209px; height: 132px;
    background: var(--paper);
    box-shadow: 0 2px 6px rgba(0,0,0,0.15);
    overflow: hidden;
  }
  .business-card .brand-name { position: absolute; left: 34px; top: 14px; font-size: 10px; }
  .business-card .brand-dot { width: 9px; height: 9px; }
  .card-band {
    position: absolute; left: 0; right: 0; top: 48px; bottom: 0;
    background: linear-gradient(180deg, var(--brand-red), var(--brand-red-dark));
    color: #fff; padding: 10px 12px;
  }
  .card-person { font-size: 9px; font-weight: 600; }
  .card-role { font-size: 7px; opacity: 0.9; margin-bottom: 6px; }
  .card-contact { list-style: none; font-size: 5.5px; line-height: 1.55; }

  /* Letterhead */
  .letterhead {
    position: absolute; left: 221px; top: 29px; width: 367px; height: 528px;
    background: var(--paper);
    box-shadow: 0 3px 10px rgba(0,0,0,0.15);
  }
  .letterhead .brand-name { position: absolute; top: 26px; left: 50%; transform: translateX(-50%); font-size: 15px; }
  .letterhead .brand-dot { width: 12px; height: 12px; }
  .watermark {
    position: absolute; left: 50%; transform: translateX(-50%);
    display: flex; flex-direction: column; align-items: center; gap: 6px;
  }
  .watermark-circle { border-radius: 50%; background: var(--faint); }
  .watermark-name {
    font-family: "Montserrat", Arial, sans-serif; font-weight: 700;
    text-transform: uppercase; color: var(--faint); white-space: nowrap;
  }
  .letterhead .watermark { top: 228px; }
  .letterhead .watermark-circle { width: 92px; height: 92px; }
  .letterhead .watermark-name { font-size: 13px; }
  .letter-footer-band {
    position: absolute; left: 0; right: 0; top: 468px; height: 18px;
    background: linear-gradient(180deg, var(--brand-red), var(--brand-red-dark));
  }
  .letter-footer {
    position: absolute; left: 0; right: 0; top: 470px;
    display: flex; justify-content: center; gap: 14px;
    font-size: 6px; color: #fff; line-height: 14px;
  }

  /* Envelope backs */
  .envelope-back {
    position: absolute; left: 720px; width: 408px; height: 190px;
    background: var(--paper);
    border-radius: 6px;
    box-shadow: 0 2px 8px rgba(0,0,0,0.15);
    overflow: hidden;
  }
  .envelope-back.red { top: 29px; }
  .envelope-back.blue { top: 132px; }
  .envelope-back.plain { top: 240px; }
  .envelope-flap {
    position: absolute; left: 0; right: 0; top: 0; height: 74px;
    border-radius: 6px 6px 28px 28px;
  }
  .red .envelope-flap { background: linear-gradient(180deg, #e2333a, var(--brand-red-dark)); }
  .blue .envelope-flap { background: linear-gradient(180deg, #3a6fc6, #1f4c97); }
  .plain svg { position: absolute; left: 0; top: 0; }

  /* Envelope front */
  .envelope-front {
    position: absolute; left: 653px; top: 348px; width: 404px; height: 204px;
    background: var(--paper);
    box-shadow: 0 3px 10px rgba(0,0,0,0.18);
  }
  .envelope-front .brand-name { position: absolute; left: 24px; top: 28px; font-size: 15px; }
  .envelope-front .brand-dot { width: 12px; height: 12px; }
  .return-address {
    position: absolute; left: 24px; top: 56px;
    font-size: 6px; color: var(--muted); line-height: 1.5;
  }
  .envelope-front .watermark { top: 110px; }
  .envelope-front .watermark-circle { width: 62px; height: 62px; }
  .envelope-front .watermark-name { font-size: 9px; }

  .option-label {
    position: absolute; top: 576px;
    font-family: "Montserrat", Arial, sans-serif; font-weight: 700;
    font-size: 8px; letter-spacing: 0.25em; text-transform: uppercase;
    color: #6e6a64; transform: translateX(-50%); white-space: nowrap;
  }
</style>
</head>
<body>

  <article class="business-card">
    <div class="brand-name"><span class="brand-dot"></span>Brightcoat finishes</div>
    <div class="card-band">
      <p class="card-person">Marek Dolvan</p>
      <p class="card-role">Owner</p>
      <ul class="card-contact">
        <li>630-555-0148</li>
        <li>marek.dolvan@brightcoatfinishes.com</li>
        <li>www.brightcoatfinishes.com</li>
        <li>318 S Harlow Ave suite 204, Villa Park, IL 60139</li>
      </ul>
    </div>
  </article>

  <article class="letterhead">
    <div class="brand-name"><span class="brand-dot"></span>Brightcoat finishes</div>
    <div class="watermark" aria-hidden="true">
      <span class="watermark-circle"></span>
      <span class="watermark-name">Brightcoat finishes</span>
    </div>
    <div class="letter-footer-band"></div>
    <div class="letter-footer">
      <span>318 S Harlow Ave suite 204, Villa Park, IL 60139</span>
      <span>630-555-0148</span>
      <span>www.brightcoatfinishes.com</span>
    </div>
  </article>
  <p class="option-label" style="left:405px">Letter head Option 1</p>

  <div class="envelope-back red"><div class="envelope-flap"></div></div>
  <div class="envelope-back blue"><div class="envelope-flap"></div></div>
  <div class="envelope-back plain">
    <svg width="408" height="190" viewBox="0 0 408 190">
      <path d="M4 4 Q204 100 404 4" fill="none" stroke="var(--hairline)" stroke-width="1.2"/>
    </svg>
  </div>

  <article class="envelope-front">
    <div class="brand-name"><span class="brand-dot"></span>Brightcoat finishes</div>
    <p class="return-address">318 S Harlow Ave suite 204<br>Villa Park, IL 60139</p>
    <div class="watermark" aria-hidden="true">
      <span class="watermark-circle"></span>
      <span class="watermark-name">Brightcoat finishes</span>
    </div>
  </article>
  <p class="option-label" style="left:863px">Envelope Option 2</p>

</body>
</html>
```